QWR Consulting Web Design… We need a Facelift!

We currently have a website but it is very outdated. We like our content, but could use some help on giving it a refreshed facelift.

www.QWR-Consulting.example is our site

We only consult with large companies in the US that have sales over $250,000 a year, so looking to be high end yet approachable in our look.

Target Market(s)

Large corporations

Industry/Entity Type

Consulting

Coding

Coded - Design and coding required

Number of Pages Required

5+ page

Font styles to use
Serif
Sans Serif

Requirements
Must have
• We love our logo, keep that the same.
• The site colors can deviate from the logo, as long as it is complimentary
Nice to have
• We like our videos and graphics. If you can make them better, then great! But you can also feel free to reuse them.
• There is a video on the opening screen and one on the video page.
• We would like the video on the video page to be incorporated on the first page.
• If you think we need other/more page, we are all ears!
Should not have
• Want to set us apart from our competition in look, feel, professionalism and step away from the old fashioned conservatives of their websites. We want to be professional, yet bolder and fresher.
• Our Competition is LedgerBrook.example and TheHallowayPartners.example, but not looking to copy of emulate them, but gives an idea of the world QWR is in.

```html
<!DOCTYPE html>
<html lang="en">
<head>
<meta charset="utf-8">
<title>QWR Consulting</title>
<link rel="stylesheet" href="https://fonts.googleapis.com/css2?family=Open+Sans:ital,wght@0,400;0,600;0,700;1,400&display=swap">
<style>
:root{
  --accent:#b3261e;
  --ink:#333;
  --muted:#777;
  --rule:#ddd;
  --band:#ececec;
  --panel:#f0f0f0;
  --dark:#2e2e2e;
  --link:#1a8fd6;
}
*{box-sizing:border-box;margin:0;padding:0}
html,body{width:741px;height:1200px;overflow:hidden}
body{position:relative;background:#fff;font-family:"Open Sans",Arial,sans-serif;color:var(--ink)}
.abs{position:absolute}
.top-band{left:0;top:0;width:741px;height:290px;background:var(--band)}
.brand{left:194px;top:6px;display:flex;align-items:center;gap:4px}
.brand-dot{width:14px;height:14px;border-radius:50%;background:var(--accent)}
.brand-name{font-size:15px;font-weight:700;color:var(--ink);letter-spacing:1px}
.brand-url{left:198px;top:27px;font-size:5.5px;font-weight:700;color:#555}
.main-nav{top:16px;font-size:6px;color:#555}
.rule{height:1px;background:var(--rule)}
.sub-nav{top:46px;font-size:4.6px;color:#666}
.sub-sep{top:45px;width:1px;height:8px;background:#bbb}
.social{top:45px;width:7px;height:7px;border-radius:50%;background:#777}
.hero{left:194px;top:60px;width:350px;height:152px;background:linear-gradient(135deg,#c9d4df,#a9b7c4 40%,#d8cbbd 70%,#eee)}
.hero-bar{left:194px;top:212px;width:350px;height:2px;background:#333}
.play{left:353px;top:118px;width:32px;height:32px;border-radius:50%;border:2px solid rgba(255,255,255,.8)}
.play::after{content:"";position:absolute;left:12px;top:8px;border-left:9px solid rgba(255,255,255,.85);border-top:6px solid transparent;border-bottom:6px solid transparent}
.intro-title{left:194px;top:229px;width:350px;text-align:center;font-size:6.8px;font-weight:400;color:var(--accent)}
.intro-text{left:194px;top:244px;width:350px;text-align:center;font-size:4.7px;line-height:8px;color:#555}
.tag{background:var(--dark);color:#fff;font-size:4.6px;letter-spacing:.5px;text-align:center;line-height:9px;height:9px}
.step-icon{top:355px}
.step-title{top:378px;font-size:5.6px;letter-spacing:.6px;color:#444}
.step-line{top:389px;width:14px;height:1px;background:#bbb}
.step-list{top:395px;list-style:none;font-size:4.8px;line-height:11.3px;color:#666}
.step-list li::before{content:"";display:inline-block;width:3px;height:3px;border-radius:50%;background:#999;margin-right:4px;vertical-align:middle}
.vsep{top:352px;width:1px;height:76px;background:var(--rule)}
.h-sec{font-size:5.6px;letter-spacing:.6px;color:#333;font-weight:400}
.h-sec b{font-weight:400;color:var(--accent)}
.market-img{left:194px;top:495px;width:86px;height:54px;background:linear-gradient(135deg,#d9dde2,#b9c3cf 50%,#eef0f2)}
.market-title{left:286px;top:492px;font-size:6px;color:#333}
.market-line{left:286px;top:505px;width:16px;height:1px;background:#bbb}
.market-text{left:286px;top:509px;width:138px;font-size:4.8px;line-height:9.6px;color:#666}
.acc{left:194px;width:230px;height:18px;border-top:1px solid var(--rule)}
.acc span{position:absolute;left:0;top:4px}
.acc i{position:absolute;right:6px;top:2px;font-style:normal;font-size:7px;color:#888}
.side{left:432px;top:481px;width:112px;height:252px;background:var(--panel)}
.why{left:443px}
.why-icon{position:absolute;left:0;top:2px}
.why-title{position:absolute;left:19px;top:0;font-size:6px;color:#333}
.why-text{position:absolute;left:19px;top:10px;width:80px;font-size:4.5px;line-height:7.4px;color:#666}
.tweet{left:0;top:748px;width:741px;height:18px;border-top:1px solid var(--rule)}
.tweet-dot{left:196px;top:754px;width:7px;height:7px;border-radius:50%;background:#888}
.tweet-text{left:217px;top:754px;font-size:4.6px;color:#666}
.tweet-text a{color:var(--link);text-decoration:none}
.testi{left:0;top:766px;width:741px;height:156px;background:radial-gradient(ellipse at 40% 40%,#3a3a3a,#111 70%,#000)}
.testi-tag{left:336px;top:797px;width:66px;background:#fff;color:#333}
.quote{left:220px;top:818px;width:300px;text-align:center;font-style:italic;font-size:6.1px;line-height:11.4px;color:#ddd}
.attr{left:194px;top:870px;width:350px;text-align:center;font-size:4.6px;letter-spacing:.3px;color:#ccc}
.attr b{color:#fff;font-weight:700}
.dots{left:361px;top:892px;display:flex;gap:2px}
.dots span{width:4px;height:4px;border-radius:50%;border:1px solid #fff}
.dots span:first-child{background:#fff}
.small-line{width:16px;height:1px;background:#bbb}
.body-text{font-size:5px;line-height:9px;color:#666}
.field{left:194px;width:172px;border:1px solid #d6d6d6;font-size:4.8px;color:#999;padding:6px 8px}
.send{left:194px;top:1129px;width:172px;height:22px;background:var(--dark);color:#fff;font-size:5.6px;letter-spacing:.6px;text-align:center;line-height:22px}
.mail{color:var(--link)}
.foot{top:1184px;font-size:4.6px;color:#888}
</style>
</head>
<body>
<div class="abs top-band"></div>

<div class="abs brand"><span class="brand-dot"></span><span class="brand-name">QWR</span></div>
<div class="abs brand-url">QWR-Consulting.example</div>

<nav>
  <span class="abs main-nav" style="left:350px">Home</span>
  <span class="abs main-nav" style="left:388px">Why QWR?</span>
  <span class="abs main-nav" style="left:432px">Our Process</span>
  <span class="abs main-nav" style="left:479px">Clients</span>
  <span class="abs main-nav" style="left:515px">Contact Us</span>
</nav>
<div class="abs rule" style="left:194px;top:40px;width:350px"></div>

<span class="abs sub-nav" style="left:194px">Peer Benchmark Modeling™</span>
<span class="abs sub-sep" style="left:278px"></span>
<span class="abs sub-nav" style="left:292px">Account Yield Modeling™</span>
<span class="abs sub-sep" style="left:383px"></span>
<span class="abs sub-nav" style="left:394px">Ledger Crawler™</span>
<span class="abs social" style="left:492px" aria-label="Social link"></span>
<span class="abs social" style="left:507px" aria-label="Social link"></span>
<span class="abs social" style="left:522px" aria-label="Social link"></span>
<span class="abs social" style="left:537px" aria-label="Social link"></span>

<div class="abs hero" role="img" aria-label="Video still: a team of four colleagues reviewing documents at a desk"></div>
<div class="abs play"></div>
<div class="abs hero-bar"></div>

<h1 class="abs intro-title">Introducing a brand-new way to manage your treasury management fees</h1>
<p class="abs intro-text">QWR Consulting works closely with your team assisting in auditing your bank fees and earnings credit rates. As former bankers, we bring our primary and regional bank experience to the table to supplement your team in providing insider knowledge for various bank pricing and net cost thresholds, so you can negotiate better pricing, rates, and terms. Maximize return when you Know Your Numbers.</p>

<div class="abs tag" style="left:343px;top:323px;width:52px">OUR PROCESS</div>

<svg class="abs step-icon" style="left:194px" width="16" height="16" viewBox="0 0 16 16" fill="#999"><circle cx="8" cy="8" r="2.5"/><circle cx="3" cy="3" r="1.6"/><circle cx="13" cy="3" r="1.6"/><circle cx="3" cy="13" r="1.6"/><circle cx="13" cy="13" r="1.6"/><circle cx="8" cy="1.5" r="1.2"/><path d="M3 3L13 13M13 3L3 13" stroke="#999" stroke-width=".8"/></svg>
<div class="abs step-title" style="left:194px">MODEL</div>
<div class="abs step-line" style="left:194px"></div>
<ul class="abs step-list" style="left:194px"><li>Gather statements</li><li>Bullet Analyze against market</li><li>Bullet Calculate profitability</li></ul>

<div class="abs vsep" style="left:308px"></div>

<svg class="abs step-icon" style="left:336px" width="16" height="16" viewBox="0 0 16 16" fill="none" stroke="#999" stroke-width="1.4"><path d="M11 3L4 10a2 2 0 003 3l7-7a3.3 3.3 0 00-5-5L2 8"/></svg>
<div class="abs step-title" style="left:336px">ENGAGE</div>
<div class="abs step-line" style="left:336px"></div>
<ul class="abs step-list" style="left:336px"><li>Review win-win strategies</li><li>Bullet Discuss with providers</li><li>Bullet Finalize agreements</li></ul>

<div class="abs vsep" style="left:430px"></div>

<svg class="abs step-icon" style="left:450px" width="16" height="16" viewBox="0 0 16 16" fill="none" stroke="#999" stroke-width="1.3"><rect x="2" y="2.5" width="11" height="13"/><rect x="5" y="1" width="5" height="3" fill="#999"/><path d="M5 10l2 2 6-7"/></svg>
<div class="abs step-title" style="left:450px">AUDIT</div>
<div class="abs step-line" style="left:450px"></div>
<ul class="abs step-list" style="left:450px"><li>Inspect pricing adherence</li><li>Bullet Continue market benchmarking</li><li>Bullet Complete contract compliance</li></ul>

<div class="abs rule" style="left:194px;top:458px;width:350px;background:#eee"></div>

<h2 class="abs h-sec" style="left:194px;top:479px">KNOW THE <b>MARKET</b></h2>
<div class="abs market-img" role="img" aria-label="Financial charts and printed reports on a desk"></div>
<div class="abs market-title">Focusing on your business – not on banking.</div>
<div class="abs market-line"></div>
<p class="abs market-text">Even in today's information age, it is exceedingly difficult to keep up with changes. That's why we supplement our industry benchmarks with our Ledger Crawler™ that scours the web for up-to-date pricing and rate changes. Hours of RFP, account analysis, publications, and other market peer comparisons reviews are automatically done for you.</p>

<div class="abs acc h-sec" style="top:587px"><span>UNDERSTAND <b>PROFITABILITY</b></span><i>+</i></div>
<div class="abs acc h-sec" style="top:605px"><span>AUGMENT YOUR <b>TEAM</b></span><i>+</i></div>
<div class="abs acc h-sec" style="top:624px"><span>WHAT BANKS <b>WANT</b></span><i>+</i></div>
<div class="abs acc h-sec" style="top:642px"><span>AVOID SWITCHING <b>PROVIDERS</b></span><i>+</i></div>
<div class="abs rule" style="left:194px;top:660px;width:230px"></div>

<aside class="abs side"></aside>
<h2 class="abs h-sec" style="left:443px;top:490px">WHY <b>QWR?</b></h2>
<div class="abs small-line" style="left:443px;top:500px"></div>

<div class="abs why" style="top:506px">
  <svg class="why-icon" width="12" height="12" viewBox="0 0 12 12" fill="#555"><rect x="1" y="8" width="2" height="4"/><rect x="4.5" y="6" width="2" height="6"/><rect x="8" y="4" width="2" height="8"/><path d="M1 6l4-3 3 2 4-4" stroke="#555" fill="none" stroke-width="1"/></svg>
  <div class="why-title">Profitability</div>
  <div class="why-text">Clients enjoy gains they never thought possible by looking beyond market pricing and harnessing AYM™</div>
</div>
<div class="abs why" style="top:552px">
  <svg class="why-icon" width="12" height="12" viewBox="0 0 12 12" fill="#555"><path d="M0 4L6 0l6 4z"/><rect x="1" y="5" width="1.5" height="5"/><rect x="4" y="5" width="1.5" height="5"/><rect x="6.5" y="5" width="1.5" height="5"/><rect x="9.5" y="5" width="1.5" height="5"/><rect x="0" y="10.5" width="12" height="1.5"/></svg>
  <div class="why-title">Insiders</div>
  <div class="why-text">Our team has managed treasury personnel as well as client relationships from within banks.</div>
</div>
<div class="abs why" style="top:590px">
  <svg class="why-icon" width="12" height="12" viewBox="0 0 12 12" fill="none" stroke="#555" stroke-width="1.8"><path d="M10 4a4.5 4.5 0 10.5 3"/></svg>
  <div class="why-title">Involved</div>
  <div class="why-text">Clients enjoy gains never possible before, with millions of dollars in actualized annual savings in their accounts.</div>
</div>
<div class="abs why" style="top:638px">
  <svg class="why-icon" width="12" height="12" viewBox="0 0 12 12" fill="none" stroke="#555" stroke-width="1.1"><rect x="1" y="1.5" width="9" height="10"/><path d="M3 7l2 2 5-6"/></svg>
  <div class="why-title">Thorough</div>
  <div class="why-text">A complete turn-key solution. We do the work, you make the decisions.</div>
</div>
<div class="abs why" style="top:678px">
  <svg class="why-icon" width="12" height="12" viewBox="0 0 12 12" fill="none" stroke="#555" stroke-width="1.1"><rect x="1" y="1" width="10" height="7.5"/><path d="M6 8.5v2M3 11h6"/></svg>
  <div class="why-title">Data</div>
  <div class="why-text">Ledger Crawler™ is our proprietary internet bot that systematically searches and indexes treasury pricing and rates.</div>
</div>

<div class="abs tweet"></div>
<span class="abs tweet-dot"></span>
<span class="abs sub-sep" style="left:210px;top:753px"></span>
<p class="abs tweet-text">Lorem Ipsum is simply dummy text of the printing and typesetting industry <a href="#">http://social.example/xdf34/jasJaj</a></p>

<section class="abs testi"></section>
<div class="abs tag testi-tag">CLIENT TESTIMONIALS</div>
<blockquote class="abs quote">In the 20 years I've been in treasury management, I really felt that I'd mastered our bank pricing. But when I started understanding bank's profitability so that I could laser focus on line items or rates for discussion, it became a game changer.</blockquote>
<div class="abs attr"><b>TREASURER OF A NATIONAL RETAIL</b> - DEPARTMENT STORE</div>
<div class="abs dots"><span></span><span></span><span></span></div>

<h2 class="abs h-sec" style="left:194px;top:957px">LEAVE A <b>MESSAGE</b></h2>
<div class="abs small-line" style="left:194px;top:968px"></div>
<p class="abs body-text" style="left:194px;top:974px;width:175px">For all of your treasury and cash management fee, earnings credit rate, merchant card and purchase card needs.</p>
<div class="abs field" style="top:998px;height:20px">Your Name*</div>
<div class="abs field" style="top:1021px;height:19px">Your Email Address*</div>
<div class="abs field" style="top:1043px;height:19px">Phone Number</div>
<div class="abs field" style="top:1065px;height:51px">Message*</div>
<div class="abs send">SEND MESSAGE</div>

<h2 class="abs h-sec" style="left:395px;top:957px">GET IN TOUCH WITH <b>US</b></h2>
<div class="abs small-line" style="left:395px;top:968px"></div>
<p class="abs body-text" style="left:395px;top:974px;width:150px">We welcome any and all feedback, so don't hesitate to reach out to us directly at:</p>
<p class="abs body-text mail" style="left:395px;top:1001px">info@QWR-Consulting.example</p>
<p class="abs body-text" style="left:395px;top:1022px"><b style="color:#333">Or mail us at</b><br>418 Harlow Crest Avenue,<br>Millbrook, GA 30000</p>

<div class="abs rule" style="left:0;top:1176px;width:741px;background:#e6e6e6"></div>
<span class="abs foot" style="left:194px">© All Right Reserved 2016. QWR</span>
<span class="abs foot" style="left:414px">Home &nbsp;|&nbsp; Why QWR? &nbsp;|&nbsp; Our Process &nbsp;|&nbsp; Clients &nbsp;|&nbsp; Contact Us</span>
</body>
</html>
```